Home Page Design for Motor Manufacturer

Hello,
please design the homepage for a manufacturer of industry motors. I am looking for a professional, clean and minimalistic design. Since this a rather conservative industry it should get a professional look but since it is a redesign there should be some modern that gives is the modern touch of innovation.
A competitor's homepage I like is:
https://www.valtrosen.com/en/
What I like about this website:
* clean, minimal, well structured design
* mega menu
For this project please find attached the wireframes (most buttons are in German but by context and Google translate you will easily figure it out; only unclear - "Messe" means "trade exhibition"). The paddings and margins are NOT exact. Also any color of backgrounds etc. chosen is not meant to represent a real color but rather to illustrate the object and maybe show there should be some background emphasis (color or image).
Wireframes:
https: //www.filquarry. com / t / pWmeTuZa8LkiBvQx
In both wireframes the only thing that is different is the Service section. I expect from the winner both designs for this service section: one with normal cart design and one with tabs as filters to search products (find image for product categories attached)
In the header use on the left the following text:
h1: "Your competent partner for industrial engines,
-transmission and drawing parts
with more than 5000 satisfied customers "
primary button: Our products
sec. button: Download catalog
and on the right side we feature one or more product images (like putting them in a nice display together).
I also think of a solid background color or subtle gradient for the hero section.
The winner should also design an open mega menu version.
Menu items in this order:
• Home page
• Gearboxes & Motors
• Engine components
• Drawing parts
• Machines & accessories
• About us
• Contact
Also create a language switch with globe symbol and DE for Germany and EN for English above the nav plus the telephone number with icon (user dummy number +49 (0) 987650432)
Output should be in Figma, Sketch or PSD.
Fonts + color to use:
header: Proza Libre, bold, # 0171A1
body: Open Sans, regular, black
Primary accent color: # 0171A1
Text black or dark gray
background: light gray, white or shade of blue
More image resources:
https://www.filquarry.com/t/RnaHwoqPEdLu5sjv
If there are any questions please do not hesitate to ask.
Target Market(s)
B2B - anyone with industrial machinery needing small motors (not car engines)
Industry/Entity Type
Manufacturing
Number of Pages Required
1 page
Requirements
Must have
- see above
Nice to have
- see above
Should not have
- see above

```html
<!DOCTYPE html>
<html lang="en">
<head>
<meta charset="utf-8">
<title>KELVA – Industrial Motors</title>
<link href="https://fonts.googleapis.com/css2?family=Open+Sans:wght@400;600;700&family=Proza+Libre:wght@600;700&display=swap" rel="stylesheet">
<style>
:root{
  --accent:#0171A1;
  --navy:#1a4d86;
  --title-blue:#1c6aa6;
  --dark:#2b2b2b;
  --nav:#333435;
  --text:#333;
  --light-blue:#e3f3fa;
  --card-gray:#f1f1f1;
  --white:#fff;
}
*{box-sizing:border-box;margin:0;padding:0}
html,body{width:1200px;height:4979px;overflow:hidden;background:var(--white)}
body{position:relative;font-family:"Open Sans",sans-serif;color:var(--text)}
.abs{position:absolute}
h1,h2,h3{font-family:"Proza Libre",sans-serif}

/* top bar */
.brand{left:73px;top:36px;display:flex;align-items:center;gap:10px;font-family:"Proza Libre",sans-serif;font-weight:700;font-size:38px;color:var(--navy);letter-spacing:1px}
.brand .dot{width:16px;height:16px;border-radius:50%;background:var(--accent)}
.top-phone{left:760px;top:18px;display:flex;align-items:center;gap:16px}
.round-icon{width:40px;height:40px;border:2px solid var(--accent);border-radius:50%;display:flex;align-items:center;justify-content:center}
.top-phone .lbl{font-size:14px;font-weight:700;color:var(--dark)}
.top-phone .num{font-size:19px;color:var(--accent);font-weight:600}
.lang{left:1064px;top:30px;font-size:15px;font-weight:700;color:var(--dark)}
.lang .on{color:var(--accent)}

.nav{left:0;top:83px;width:1200px;height:54px;background:var(--nav);display:flex;align-items:center;padding-left:73px;gap:42px}
.nav a{color:#fff;text-decoration:none;font-size:13px;font-weight:600;text-transform:uppercase}
.nav a.active{color:#5cc3ee}

/* hero */
.hero{left:0;top:137px;width:1200px;height:730px;background:linear-gradient(90deg,#1f9ac7 0%,#2fb2d9 55%,#7fd3ec 100%);clip-path:polygon(0 0,100% 0,100% 632px,0 730px)}
.hero-title{left:75px;top:262px;width:640px;font-size:36px;line-height:49px;color:#fff;font-weight:700;letter-spacing:.5px}
.btn{display:inline-flex;align-items:center;gap:10px;background:var(--navy);color:#fff;font-size:14px;font-weight:700;text-transform:uppercase;padding:0 22px;height:42px;text-decoration:none;letter-spacing:.3px}
.btn .arr{width:13px;height:13px;border-radius:50%;background:#fff;display:inline-flex;align-items:center;justify-content:center}
.hero-btns{left:75px;top:543px;display:flex;gap:14px}
.hero-btns .btn{height:40px;padding:0 22px}
.hero-btns .btn.sec{background:#1a68a8}
.reducer{left:795px;top:168px;width:350px;height:370px;border-radius:50%;background:radial-gradient(circle at 50% 50%,#5b646c 0%,#8f979e 22%,#e3e6e9 45%,#b9bec4 75%,#8a9096 100%)}
.gearbox{left:590px;top:430px;width:330px;height:245px;border-radius:60px 30px 40px 90px;background:linear-gradient(135deg,#d9dde1 0%,#8e959b 30%,#2c3034 55%,#55595e 80%,#c7ccd1 100%)}
.benefits{left:73px;top:715px;display:flex;gap:29px}
.benefit{width:242px;height:209px;border:4px solid #e9e9e9;display:flex;align-items:center;justify-content:center;color:#fff;font-family:"Proza Libre",sans-serif;font-weight:700;font-size:23px;letter-spacing:1px}
.b1{background:linear-gradient(135deg,#5f7a8a,#25343f)}
.b2{background:linear-gradient(135deg,#6f8aa5,#2b3a52)}
.b3{background:linear-gradient(135deg,#3b5f7c,#8a6a3a)}
.b4{background:linear-gradient(135deg,#4f5d60,#273135)}

.sec-title{width:1200px;left:0;text-align:center;font-size:33px;font-weight:700;color:var(--dark);letter-spacing:1px}

/* products */
.product{width:514px;height:442px}
.product .img{width:514px;height:302px;background:var(--card-gray);display:flex;align-items:center;justify-content:center}
.product .img .shape{width:300px;height:200px;border-radius:50px;background:linear-gradient(135deg,#2a2d31,#7c8389 60%,#c9ced3)}
.product .body{position:absolute;left:20px;top:270px;width:474px;background:#fff;text-align:center;padding-top:22px}
.product h3{font-size:20px;color:var(--title-blue);font-weight:700;letter-spacing:.5px}
.product p{font-size:15.5px;line-height:26px;margin-top:6px;color:var(--text)}
.product .btn{margin-top:32px;height:42px;padding:0 29px}

/* measure up */
.measure-bg{left:0;top:2063px;width:1200px;height:1145px;background:var(--light-blue);clip-path:polygon(0 0,100% 82px,100% 1145px,0 1066px)}
.mcard{width:1050px;height:236px;background:#fff;box-shadow:0 6px 0 -1px var(--accent)}
.mcard .img{position:absolute;top:0;width:333px;height:236px}
.mcard .txt{position:absolute;top:28px;width:640px}
.mcard h3{font-size:19px;color:var(--title-blue);font-weight:700;letter-spacing:.5px}
.mcard p{font-size:15px;line-height:26px;margin-top:12px}
.mcard .btns{margin-top:20px;display:flex;gap:12px}
.mcard .btn{height:42px;padding:0 16px}

/* about */
.about-photo{top:3265px;width:242px;height:352px}
.about h2{font-size:34px;font-weight:700;color:var(--dark);letter-spacing:1px}
.about p{font-size:14.5px;line-height:31.5px;margin-top:18px;width:520px}
.about .btn{margin-top:28px;height:45px;padding:0 33px}

/* downloads */
.dl-bg{left:0;top:3680px;width:1200px;height:480px;background:var(--light-blue);clip-path:polygon(0 0,100% 70px,100% 480px,0 445px)}
.downloads h2{font-size:34px;font-weight:700;color:var(--dark);letter-spacing:1px}
.downloads p{font-size:15px;line-height:31.5px;margin-top:14px;width:600px}
.downloads .btn{margin-top:24px;height:46px;padding:0 27px}
.brochure{left:782px;top:3816px;width:300px;height:270px;background:linear-gradient(135deg,#f4f7fa,#cfdce8);transform:rotate(15deg);box-shadow:0 8px 18px rgba(0,0,0,.2)}

/* contact */
.contact-bg{left:0;top:4125px;width:1200px;height:515px;background:linear-gradient(90deg,#0c5f95,#1684b4);clip-path:polygon(0 0,100% 40px,100% 455px,0 515px)}
.people{left:0;top:4240px;width:695px;height:395px;background:linear-gradient(180deg,#2e4a7a,#142a58)}
.contact h2{font-size:34px;font-weight:700;color:#fff;letter-spacing:1px}
.c-item{display:flex;align-items:center;gap:20px;color:#fff}
.c-item .round-icon{border-color:#fff;width:52px;height:52px}
.c-item .lbl{font-size:15px;font-weight:700}
.c-item .val{font-size:19px;font-weight:700;font-family:"Proza Libre",sans-serif}

/* footer */
.foot-brand{left:73px;top:4712px}
.copy{left:73px;top:4803px;font-size:12px;line-height:21px;color:var(--dark)}
.social{left:73px;top:4857px;display:flex;gap:18px}
.social span{width:15px;height:15px;border-radius:50%;background:var(--dark)}
.fcol h4{font-size:16px;font-weight:700;color:var(--title-blue);font-family:"Proza Libre",sans-serif;letter-spacing:.5px;margin-bottom:8px}
.fcol a{display:block;font-size:14px;line-height:31.5px;color:var(--dark);text-decoration:none}
</style>
</head>
<body>

<div class="abs brand"><span>KELVA</span><span class="dot"></span></div>
<div class="abs top-phone">
  <div class="round-icon"><svg width="18" height="18" viewBox="0 0 24 24"><path fill="#0171A1" d="M6.6 10.8a15.1 15.1 0 0 0 6.6 6.6l2.2-2.2a1 1 0 0 1 1-.25 11.4 11.4 0 0 0 3.6.57 1 1 0 0 1 1 1V20a1 1 0 0 1-1 1A17 17 0 0 1 3 4a1 1 0 0 1 1-1h3.5a1 1 0 0 1 1 1c0 1.25.2 2.45.57 3.57a1 1 0 0 1-.25 1z"/></svg></div>
  <div><div class="lbl">PHONE:</div><div class="num">+49 (0) 987650432</div></div>
</div>
<div class="abs lang"><span class="on">EN</span> | DE</div>

<nav class="abs nav">
  <a class="active" href="#">Home</a>
  <a href="#">Gearboxes &amp; Motors</a>
  <a href="#">Engine components</a>
  <a href="#">Drawing parts</a>
  <a href="#">Machines &amp; accessories</a>
  <a href="#">About us</a>
  <a href="#">Contact</a>
</nav>

<section class="abs hero"></section>
<div class="abs reducer" role="img" aria-label="Precision strain wave reducer"></div>
<div class="abs gearbox" role="img" aria-label="Right angle planetary gearbox"></div>
<h1 class="abs hero-title">Your competent partner for<br>industrial engines, transmission<br>and drawing parts with more<br>than 5000 satisfied<br>customers.</h1>
<div class="abs hero-btns">
  <a class="btn" href="#">Our products <span class="arr"><svg width="7" height="7" viewBox="0 0 8 8"><path d="M2.5 1l3 3-3 3" stroke="#1a4d86" stroke-width="1.6" fill="none"/></svg></span></a>
  <a class="btn sec" href="#">Download catalog <span class="arr"><svg width="7" height="7" viewBox="0 0 8 8"><path d="M2.5 1l3 3-3 3" stroke="#1a68a8" stroke-width="1.6" fill="none"/></svg></span></a>
</div>
<div class="abs benefits">
  <div class="benefit b1" role="img" aria-label="Photo of production line">BENEFITS</div>
  <div class="benefit b2" role="img" aria-label="Photo of a business meeting">BENEFITS</div>
  <div class="benefit b3" role="img" aria-label="Photo of machining work">BENEFITS</div>
  <div class="benefit b4" role="img" aria-label="Photo of an industrial machine">BENEFITS</div>
</div>

<h2 class="abs sec-title" style="top:992px">PRODUCTS</h2>
<div class="abs product" style="left:73px;top:1076px">
  <div class="img"><div class="shape" role="img" aria-label="AC gear motor"></div></div>
  <div class="body"><h3>PRODUCT TITLE</h3><p>Neque porro quisquam est qui dolorem ipsum<br>quia dolor sit amet consectetur.</p><a class="btn" href="#">Details <span class="arr"><svg width="7" height="7" viewBox="0 0 8 8"><path d="M2.5 1l3 3-3 3" stroke="#1a4d86" stroke-width="1.6" fill="none"/></svg></span></a></div>
</div>
<div class="abs product" style="left:614px;top:1076px">
  <div class="img"><div class="shape" role="img" aria-label="Planetary gearbox"></div></div>
  <div class="body"><h3>PRODUCT TITLE</h3><p>Neque porro quisquam est qui dolorem ipsum<br>quia dolor sit amet consectetur.</p><a class="btn" href="#">Details <span class="arr"><svg width="7" height="7" viewBox="0 0 8 8"><path d="M2.5 1l3 3-3 3" stroke="#1a4d86" stroke-width="1.6" fill="none"/></svg></span></a></div>
</div>
<div class="abs product" style="left:73px;top:1550px">
  <div class="img"><div class="shape" role="img" aria-label="DC planetary gear motor"></div></div>
  <div class="body"><h3>PRODUCT TITLE</h3><p>Neque porro quisquam est qui dolorem ipsum<br>quia dolor sit amet consectetur.</p><a class="btn" href="#">Details <span class="arr"><svg width="7" height="7" viewBox="0 0 8 8"><path d="M2.5 1l3 3-3 3" stroke="#1a4d86" stroke-width="1.6" fill="none"/></svg></span></a></div>
</div>
<div class="abs product" style="left:614px;top:1550px">
  <div class="img"><div class="shape" role="img" aria-label="Right angle gearbox"></div></div>
  <div class="body"><h3>PRODUCT TITLE</h3><p>Neque porro quisquam est qui dolorem ipsum<br>quia dolor sit amet consectetur.</p><a class="btn" href="#">Details <span class="arr"><svg width="7" height="7" viewBox="0 0 8 8"><path d="M2.5 1l3 3-3 3" stroke="#1a4d86" stroke-width="1.6" fill="none"/></svg></span></a></div>
</div>

<div class="abs measure-bg"></div>
<h2 class="abs sec-title" style="top:2192px">MEASURE UP</h2>

<div class="abs mcard" style="left:70px;top:2270px">
  <div class="img" style="left:3px;background:linear-gradient(135deg,#cfd6dc,#6d7780)" role="img" aria-label="Photo of gearboxes on exhibition display"></div>
  <div class="txt" style="left:378px"><h3>MEASURE UP TITLE</h3><p>Neque porro quisquam est qui dolorem ipsum quia dolor sit amet consectetur. Aenean in lectus eget erat molestie hendrerit. Curabitur elementum quis dolor et efficitur. Integer at orci at urna fermentum cursus.</p>
  <div class="btns"><a class="btn" href="#">Free tickts <span class="arr"><svg width="7" height="7" viewBox="0 0 8 8"><path d="M2.5 1l3 3-3 3" stroke="#1a4d86" stroke-width="1.6" fill="none"/></svg></span></a><a class="btn" href="#">Details <span class="arr"><svg width="7" height="7" viewBox="0 0 8 8"><path d="M2.5 1l3 3-3 3" stroke="#1a4d86" stroke-width="1.6" fill="none"/></svg></span></a></div></div>
</div>

<div class="abs mcard" style="left:78px;top:2545px">
  <div class="txt" style="left:35px"><h3>MEASURE UP TITLE</h3><p>Neque porro quisquam est qui dolorem ipsum quia dolor sit amet consectetur. Aenean in lectus eget erat molestie hendrerit. Curabitur elementum quis dolor et efficitur. Integer at orci at urna fermentum cursus.</p>
  <div class="btns"><a class="btn" href="#">Free tickts <span class="arr"><svg width="7" height="7" viewBox="0 0 8 8"><path d="M2.5 1l3 3-3 3" stroke="#1a4d86" stroke-width="1.6" fill="none"/></svg></span></a><a class="btn" href="#">Details <span class="arr"><svg width="7" height="7" viewBox="0 0 8 8"><path d="M2.5 1l3 3-3 3" stroke="#1a4d86" stroke-width="1.6" fill="none"/></svg></span></a></div></div>
  <div class="img" style="left:717px;background:linear-gradient(135deg,#e9ecef,#4d545b)" role="img" aria-label="Photo of precision reducers"></div>
</div>

<div class="abs mcard" style="left:70px;top:2819px">
  <div class="img" style="left:3px;background:linear-gradient(135deg,#9fc0cc,#2f4750)" role="img" aria-label="Photo of a gear tooth being measured"></div>
  <div class="txt" style="left:378px"><h3>MEASURE UP TITLE</h3><p>Neque porro quisquam est qui dolorem ipsum quia dolor sit amet consectetur. Aenean in lectus eget erat molestie hendrerit. Curabitur elementum quis dolor et efficitur. Integer at orci at urna fermentum cursus.</p>
  <div class="btns"><a class="btn" href="#">Free tickts <span class="arr"><svg width="7" height="7" viewBox="0 0 8 8"><path d="M2.5 1l3 3-3 3" stroke="#1a4d86" stroke-width="1.6" fill="none"/></svg></span></a><a class="btn" href="#">Details <span class="arr"><svg width="7" height="7" viewBox="0 0 8 8"><path d="M2.5 1l3 3-3 3" stroke="#1a4d86" stroke-width="1.6" fill="none"/></svg></span></a></div></div>
</div>

<div class="abs about-photo" style="left:73px;background:linear-gradient(160deg,#6b8fb4,#2d3f57)" role="img" aria-label="Photo of the company trade fair booth"></div>
<div class="abs about-photo" style="left:344px;background:linear-gradient(160deg,#3c6fb0,#c7d3de)" role="img" aria-label="Photo of the exhibition stand"></div>
<div class="abs about" style="left:615px;top:3255px">
  <h2>ABOUT US</h2>
  <p>Korvan Motor is established in Aug. 2006, and is specialized in the development, production, sales and service of the drive technology, especially the precision gears, planetary gears, gear motors, as well as motors and motor controls. The production area of Korvan Motor is around 70,000 m² and we have 1120 employees worldwide. Korvan Motor is authorized on a shares of the Meridian Stock on 29.08.2017 (Stock code: 004718).</p>
  <a class="btn" href="#">Read more <span class="arr"><svg width="7" height="7" viewBox="0 0 8 8"><path d="M2.5 1l3 3-3 3" stroke="#1a4d86" stroke-width="1.6" fill="none"/></svg></span></a>
</div>

<div class="abs dl-bg"></div>
<div class="abs downloads" style="left:87px;top:3800px">
  <h2>DOWNLOADS</h2>
  <p>Vestibulum ante ipsum primis in faucibus orci luctus et ultrices posuere cubilia curae; Aliquam est mi, vehicula ut dolor vel, pharetra efficitur velitenean in lectus eget erat molestie hendrerit. Curabitur elementum quis dolor et efficitur. Integer at orci at urna fermentum cursus. Cras elementum arcu id nunc egestas maximus.</p>
  <a class="btn" href="#">Downloads <span class="arr"><svg width="7" height="7" viewBox="0 0 8 8"><path d="M2.5 1l3 3-3 3" stroke="#1a4d86" stroke-width="1.6" fill="none"/></svg></span></a>
</div>
<div class="abs brochure" role="img" aria-label="Product catalog brochure"></div>

<div class="abs contact-bg"></div>
<div class="abs people" role="img" aria-label="Photo of two sales representatives" style="clip-path:polygon(0 0,100% 0,100% 360px,0 395px)"></div>
<div class="abs contact" style="left:618px;top:4308px"><h2>CONTACT US</h2></div>
<div class="abs c-item" style="left:618px;top:4392px">
  <div class="round-icon"><svg width="22" height="22" viewBox="0 0 24 24"><path fill="#fff" d="M6.6 10.8a15.1 15.1 0 0 0 6.6 6.6l2.2-2.2a1 1 0 0 1 1-.25 11.4 11.4 0 0 0 3.6.57 1 1 0 0 1 1 1V20a1 1 0 0 1-1 1A17 17 0 0 1 3 4a1 1 0 0 1 1-1h3.5a1 1 0 0 1 1 1c0 1.25.2 2.45.57 3.57a1 1 0 0 1-.25 1z"/></svg></div>
  <div><div class="lbl">PHONE:</div><div class="val">+49 (0) 987650432</div></div>
</div>
<div class="abs c-item" style="left:925px;top:4392px">
  <div class="round-icon"><svg width="22" height="22" viewBox="0 0 24 24"><rect x="3" y="5" width="18" height="14" rx="1.5" fill="none" stroke="#fff" stroke-width="2"/><path d="M3.5 6l8.5 7 8.5-7" fill="none" stroke="#fff" stroke-width="2"/></svg></div>
  <div><div class="lbl">PHONE:</div><div class="val">info@kelva.de</div></div>
</div>

<div class="abs brand foot-brand"><span>KELVA</span><span class="dot"></span></div>
<div class="abs copy">Copyright © 2020 CompanyName<br>All rights reserved.</div>
<div class="abs social"><span></span><span></span><span></span><span></span><span></span></div>

<div class="abs fcol" style="left:342px;top:4681px">
  <h4>SITE MAP</h4>
  <a href="#">Home</a><a href="#">Gearboxes &amp; Motors</a><a href="#">Engine components</a><a href="#">Drawing parts</a><a href="#">Machines &amp; accessories</a><a href="#">About us</a><a href="#">Contact</a>
</div>
<div class="abs fcol" style="left:616px;top:4681px">
  <h4>PRODUCTS</h4>
  <a href="#">AC DC gearmotors</a><a href="#">AC DC right angle gearmotors</a><a href="#">DC brushless gearmotors</a><a href="#">Planetary gearmotors</a><a href="#">Planetary gearboxes KX/KV</a>
</div>
<div class="abs fcol" style="left:931px;top:4681px">
  <h4>FAIRS &amp; NEWS</h4>
  <a href="#">Recent Fairs</a><a href="#">Past fairs</a><a href="#">News</a>
</div>

</body>
</html>
```